Loyalty card for customers

I would like logo an a section for 10 places, so I can advertise 10th float is free, our business is health and wellness we offer magnesium float, hyperbaric oxygen and infrared sauna

```html
<!DOCTYPE html>
<html lang="en">
<head>
<meta charset="utf-8">
<title>Loyalty Reward Card</title>
<link rel="stylesheet" href="https://fonts.googleapis.com/css2?family=Oswald:wght@600&family=Montserrat:wght@300;400;600&display=swap">
<style>
  :root {
    --canvas: #2b2b2d;
    --card-blue: #93d1ea;
    --panel-blue: #8ecfe9;
    --brand-blue: #2c9fd9;
    --soft-blue: #7ec6e6;
    --white: #ffffff;
    --ink: #141414;
    --ornament: rgba(20, 28, 34, 0.3);
  }
  * { box-sizing: border-box; margin: 0; padding: 0; }
  html, body { width: 1200px; height: 900px; overflow: hidden; }
  body { background: var(--canvas); position: relative; font-family: "Montserrat", sans-serif; }

  .card { position: absolute; border-radius: 18px; overflow: hidden; }

  /* Front */
  .card-front {
    left: 60px; top: 278px; width: 600px; height: 343px;
    background: var(--card-blue);
    display: flex; flex-direction: column; align-items: center; justify-content: center;
  }
  .ornament { background: var(--ornament); border-radius: 40px; }
  .front-ornament { width: 170px; height: 26px; }
  .front-title-row { display: flex; align-items: center; gap: 18px; margin: 8px 0 2px; }
  .rule { width: 48px; height: 2px; background: var(--ink); }
  .front-title {
    font-family: "Oswald", sans-serif; font-weight: 600; font-size: 84px;
    line-height: 1; color: var(--white); letter-spacing: 1px;
  }
  .front-subtitle {
    font-family: "Oswald", sans-serif; font-weight: 600; font-size: 22px;
    letter-spacing: 9px; color: var(--ink); margin-bottom: 10px;
  }

  /* Back */
  .card-back {
    left: 720px; top: 100px; width: 400px; height: 700px;
    background: var(--white);
  }
  .brand-block { position: absolute; left: 0; top: 0; width: 100%; height: 260px; text-align: center; }
  .brand-ornament { position: absolute; left: 110px; top: 34px; width: 180px; height: 30px; }
  .brand-rules { position: absolute; left: 30px; right: 30px; top: 48px; display: flex; justify-content: space-between; }
  .brand-rules .rule { width: 60px; }
  .brand-name {
    position: absolute; left: 0; right: 0; top: 96px;
    font-weight: 600; font-size: 40px; line-height: 1.15;
    letter-spacing: 6px; color: var(--brand-blue);
  }
  .brand-tagline {
    position: absolute; left: 0; right: 0; top: 208px;
    font-weight: 400; font-size: 14px; letter-spacing: 6px; color: var(--soft-blue);
  }
  .divider { position: absolute; left: 24px; right: 24px; top: 262px; border-top: 3px dotted #222; }

  .stamp-panel {
    position: absolute; left: 20px; top: 284px; width: 360px; height: 396px;
    background: var(--panel-blue); border-radius: 22px;
  }
  .stamp-grid {
    position: absolute; left: 36px; top: 26px;
    display: grid; grid-template-columns: repeat(3, 82px); gap: 14px 17px;
  }
  .stamp {
    width: 82px; height: 82px; border-radius: 50%; background: var(--white);
    display: flex; align-items: center; justify-content: center;
  }
  .stamp span {
    width: 68px; height: 68px; border-radius: 50%; border: 1.5px dotted #333;
    display: flex; align-items: center; justify-content: center;
    font-weight: 300; font-size: 34px; color: var(--ink);
  }
  .reward { position: absolute; left: 36px; top: 300px; display: flex; align-items: center; gap: 16px; }
  .stamp-final { background: var(--ink); }
  .stamp-final span { border-color: var(--white); color: var(--white); }
  .reward-text { font-weight: 400; font-size: 17px; color: var(--ink); line-height: 1.3; }
  .reward-text strong { display: block; font-weight: 400; font-size: 20px; letter-spacing: 1px; }
</style>
</head>
<body>

<section class="card card-front" aria-label="Card front">
  <div class="ornament front-ornament" role="img" aria-label="Decorative flourish"></div>
  <div class="front-title-row">
    <span class="rule"></span>
    <h1 class="front-title">LOYALTY</h1>
    <span class="rule"></span>
  </div>
  <p class="front-subtitle">REWARD CARD</p>
  <div class="ornament front-ornament" role="img" aria-label="Decorative flourish"></div>
</section>

<section class="card card-back" aria-label="Card back">
  <div class="brand-block">
    <div class="brand-rules"><span class="rule"></span><span class="rule"></span></div>
    <div class="ornament brand-ornament" role="img" aria-label="Decorative flourish"></div>
    <p class="brand-name">Stillwater<br>Floats</p>
    <p class="brand-tagline">YOUR LOYALTY</p>
  </div>
  <div class="divider"></div>

  <div class="stamp-panel">
    <div class="stamp-grid">
      <div class="stamp"><span>1</span></div>
      <div class="stamp"><span>2</span></div>
      <div class="stamp"><span>3</span></div>
      <div class="stamp"><span>4</span></div>
      <div class="stamp"><span>5</span></div>
      <div class="stamp"><span>6</span></div>
      <div class="stamp"><span>7</span></div>
      <div class="stamp"><span>8</span></div>
      <div class="stamp"><span>9</span></div>
    </div>
    <div class="reward">
      <div class="stamp stamp-final"><span>10</span></div>
      <p class="reward-text">10th Float is<strong>ABSOLUTELY FREE</strong></p>
    </div>
  </div>
</section>

</body>
</html>
```